Business Card Design Project

Corvexa logo will be provided after
Front

Bram Oskarsen- Construction Manager

Ph: (61) 07 53182907
boskarsen@corvexa.com.au
PO Box 83 Kelbarra 4529

Back
Corvexa
EPCM

Oil - Gas - Mining

Industry/Entity Type

Business

Font styles to use
Sans Serif

Colors
faa54b

Requirements
Must have
• White Back Ground

```html
<!DOCTYPE html>
<html lang="en">
<head>
<meta charset="utf-8">
<title>Corvexa Business Card</title>
<link href="https://fonts.googleapis.com/css2?family=Source+Sans+3:wght@400;600;700;800&display=swap" rel="stylesheet">
<style>
  :root {
    --backdrop: #e9e9ec;
    --card: #ffffff;
    --ink: #111111;
    --accent: #faa54b;
    --shadow: rgba(0, 0, 0, 0.22);
  }
  html, body {
    margin: 0;
    padding: 0;
    width: 1200px;
    height: 1000px;
    overflow: hidden;
    background: var(--backdrop);
    font-family: "Source Sans 3", Arial, sans-serif;
    color: var(--ink);
  }
  .canvas {
    position: relative;
    width: 1200px;
    height: 1000px;
  }
  .card {
    position: absolute;
    left: 265px;
    width: 665px;
    height: 397px;
    background: var(--card);
    border-radius: 22px;
    box-shadow: 0 4px 14px var(--shadow);
  }
  .card--front { top: 73px; }
  .card--back { top: 532px; }

  .wordmark {
    position: absolute;
    margin: 0;
    font-weight: 800;
    letter-spacing: 0.04em;
    text-transform: uppercase;
    color: var(--ink);
    line-height: 1;
  }
  .card--front .wordmark {
    left: 0;
    right: 0;
    top: 165px;
    text-align: center;
    font-size: 66px;
  }
  .tagline {
    position: absolute;
    left: 0;
    right: 0;
    top: 256px;
    margin: 0;
    text-align: center;
    font-weight: 700;
    font-size: 16px;
    letter-spacing: 0.02em;
  }
  .card--back .wordmark {
    right: 32px;
    top: 76px;
    font-size: 42px;
  }
  .person {
    position: absolute;
    left: 33px;
    top: 174px;
  }
  .person__name {
    margin: 0;
    font-weight: 700;
    font-size: 22px;
    line-height: 1.1;
  }
  .person__role {
    margin: 0;
    color: var(--accent);
    font-size: 16px;
    line-height: 1.2;
  }
  .contact {
    position: absolute;
    left: 33px;
    top: 276px;
    margin: 0;
    padding: 0;
    list-style: none;
    font-size: 16px;
  }
  .contact__item {
    display: flex;
    align-items: center;
    gap: 8px;
    height: 22px;
  }
  .contact__item--address { margin-top: 8px; }
  .contact__icon {
    width: 14px;
    height: 14px;
    fill: var(--ink);
    flex: none;
  }
</style>
</head>
<body>
<main class="canvas">
  <section class="card card--front" aria-label="Card front">
    <h1 class="wordmark">Corvexa</h1>
    <p class="tagline">OIL - GAS - MINING</p>
  </section>

  <section class="card card--back" aria-label="Card back">
    <p class="wordmark">Corvexa</p>
    <div class="person">
      <h2 class="person__name">Bram Oskarsen</h2>
      <p class="person__role">Construction Manager</p>
    </div>
    <ul class="contact">
      <li class="contact__item">
        <svg class="contact__icon" viewBox="0 0 24 24" aria-hidden="true"><path d="M6.6 10.8c1.4 2.8 3.8 5.1 6.6 6.6l2.2-2.2c.3-.3.7-.4 1-.2 1.1.4 2.3.6 3.6.6.6 0 1 .4 1 1V20c0 .6-.4 1-1 1C10.6 21 3 13.4 3 4c0-.6.4-1 1-1h3.5c.6 0 1 .4 1 1 0 1.3.2 2.5.6 3.6.1.3 0 .7-.2 1z"/></svg>
        <span>(61) 07 53182907</span>
      </li>
      <li class="contact__item">
        <svg class="contact__icon" viewBox="0 0 24 24" aria-hidden="true"><path d="M2 5h20v14H2z M2 5l10 8 10-8" /><path d="M2 6.5l10 7.5 10-7.5V5H2z" fill="#fff"/><path d="M2 5h20L12 12.5z" /></svg>
        <span>boskarsen@corvexa.com.au</span>
      </li>
      <li class="contact__item contact__item--address">
        <svg class="contact__icon" viewBox="0 0 24 24" aria-hidden="true"><path d="M12 2C8.1 2 5 5.1 5 9c0 5.2 7 13 7 13s7-7.8 7-13c0-3.9-3.1-7-7-7zm0 9.5a2.5 2.5 0 1 1 0-5 2.5 2.5 0 0 1 0 5z"/></svg>
        <span>PO Box 83 Kelbarra 4529</span>
      </li>
    </ul>
  </section>
</main>
</body>
</html>
```